Commercial Landscaping Flyer Needed

Looking for a flyer design to showcase what we offer for commercial landscape Installations. We want this to illustrate what sets us apart from our competitors. Include our EMR Safety rating of .72, that our average commercial landscape installation size is $215,000 with our largest completed in 2020 being $1,375,590. We have backgrounds in commercial design and installation and help our customers with Value Engineering Strategies. Since incorporating in 2005, we have an average employment retention length of 8 years. We want this flyer to show our commercial clients that we mean business and are dedicated to making their project happen on time, run efficiently, and we do excellent work.

Need extra days to review

```html
<!DOCTYPE html>
<html lang="en">
<head>
<meta charset="utf-8">
<title>Verdant Works – Commercial Landscape Installations</title>
<link rel="stylesheet" href="https://fonts.googleapis.com/css2?family=League+Spartan:wght@700;800&family=Questrial&display=swap">
<style>
:root{
  --stage:#535353;
  --lime:#c2db2f;
  --ink:#000;
  --sky:#9cc4e6;
}
*{margin:0;padding:0;box-sizing:border-box}
html,body{width:1200px;height:1200px;overflow:hidden;background:var(--stage)}
.flyer{position:absolute;left:247px;top:100px;width:713px;height:1008px;overflow:hidden;font-family:"Questrial",sans-serif;color:var(--ink)}
.flyer-shapes{position:absolute;left:0;top:0;width:713px;height:1008px}
.abs{position:absolute}
.headline{left:45px;top:420px;font-family:"League Spartan",sans-serif;font-weight:800;font-size:34px;line-height:29.5px;letter-spacing:.6px;text-transform:uppercase;white-space:nowrap}
.benefits{left:44px;top:524px;width:262px;list-style:none}
.benefits li{position:relative;padding-left:24px;font-size:15px;line-height:17px;margin-bottom:11px}
.benefits li svg{position:absolute;left:0;top:1px;width:16px;height:16px}
.benefits .narrow{width:205px}
.benefits .first{width:216px}
.divider{left:333px;top:400px;width:1px;height:260px;background:var(--ink)}
.clients-title{left:366px;top:457px;font-family:"League Spartan",sans-serif;font-weight:700;font-size:14px;line-height:15px;text-transform:uppercase}
.client-list{list-style:none;font-size:12.6px;line-height:12px;white-space:nowrap}
.client-list li{position:relative;padding-left:9px;margin-bottom:4.3px}
.client-list li::before{content:"";position:absolute;left:0;top:4px;width:4px;height:4px;border-radius:50%;background:var(--ink)}
.clients-a{left:366px;top:496px}
.clients-b{left:540px;top:545px}
.safety{left:315px;top:770px;width:128px;text-align:center;font-size:17px;line-height:18.5px}
.safety .figure{display:block;font-family:"League Spartan",sans-serif;font-weight:800;font-size:38px;line-height:38px;margin-top:3px}
.since{left:315px;top:903px;width:128px;text-align:center;color:var(--lime);font-size:15px;line-height:15px}
.since .year{display:block;font-size:28px;line-height:32px}
.contact{right:56px;top:0;width:320px;height:1008px;color:var(--lime)}
.contact-item{position:absolute;right:0;text-align:right;white-space:nowrap}
.contact svg{position:absolute;right:-22px;width:17px;height:17px}
.address{top:797px;font-size:16px;line-height:17px}
.address svg{top:1px}
.office{font-size:15px;line-height:16px}
.phone{font-size:20px;line-height:22px}
.phone svg{top:3px}
.office-a{top:850px}
.phone-a{top:866px}
.office-b{top:893px}
.phone-b{top:909px}
.web{top:954px;font-size:14.5px;line-height:17px}
.web svg{top:0}
.brand{left:50px;top:882px;width:180px;text-align:center}
.brand-name{font-size:20px;line-height:22px;letter-spacing:-.3px;white-space:nowrap}
.brand-tag{font-size:7px;letter-spacing:1.5px;text-transform:uppercase;margin-top:4px;white-space:nowrap}
</style>
</head>
<body>
<main class="flyer">
  <svg class="flyer-shapes" viewBox="0 0 1140 1612" preserveAspectRatio="none">
    <defs>
      <linearGradient id="photoTone" x1="0" y1="0" x2="0" y2="1">
        <stop offset="0" stop-color="var(--sky)"/>
        <stop offset=".28" stop-color="#6f9a4c"/>
        <stop offset=".6" stop-color="#8fbf3e"/>
        <stop offset="1" stop-color="#b5d64a"/>
      </linearGradient>
    </defs>
    <rect class="hero-photo" role="img" aria-label="Photo of a landscaped commercial entrance sign with colourful flower beds and trees" x="0" y="0" width="1140" height="980" fill="url(#photoTone)"/>
    <path class="wave-band" fill="var(--ink)" d="M0 600 C150 520 300 440 480 465 C650 490 760 580 880 680 C960 750 1060 770 1140 840 L1140 1612 L0 1612 Z"/>
    <path class="content-panel" fill="var(--lime)" d="M0 660 C150 600 320 510 480 522 C640 535 760 640 860 740 C940 820 1040 830 1100 870 C1125 890 1135 920 1140 940 L1140 1225 C1000 1230 880 1200 780 1150 C700 1110 640 1090 600 1100 C520 1120 460 1200 400 1300 C330 1420 200 1480 0 1520 Z"/>
    <circle class="safety-badge" cx="606" cy="1308" r="100" fill="var(--lime)"/>
    <g class="brand-badge">
      <circle cx="170" cy="1462" r="100" fill="none" stroke="var(--ink)" stroke-width="8"/>
      <circle cx="272" cy="1440" r="104" fill="none" stroke="var(--ink)" stroke-width="8"/>
      <circle cx="170" cy="1462" r="96" fill="var(--lime)"/>
      <circle cx="272" cy="1440" r="100" fill="var(--lime)"/>
    </g>
  </svg>

  <h1 class="abs headline">Commercial<br>Landscape<br>Installations</h1>

  <ul class="abs benefits">
    <li class="first"><svg viewBox="0 0 16 16"><circle cx="8" cy="8" r="6.8" fill="none" stroke="#000" stroke-width="1.4"/><path d="M4.5 8.2l2.6 2.6L14 3" fill="none" stroke="#000" stroke-width="1.8"/></svg>Our average commercial landscape installation size is $215,000.</li>
    <li class="narrow"><svg viewBox="0 0 16 16"><circle cx="8" cy="8" r="6.8" fill="none" stroke="#000" stroke-width="1.4"/><path d="M4.5 8.2l2.6 2.6L14 3" fill="none" stroke="#000" stroke-width="1.8"/></svg>Largest completed in 2020 being $1,375,590.</li>
    <li><svg viewBox="0 0 16 16"><circle cx="8" cy="8" r="6.8" fill="none" stroke="#000" stroke-width="1.4"/><path d="M4.5 8.2l2.6 2.6L14 3" fill="none" stroke="#000" stroke-width="1.8"/></svg>We help our customers with Value Engineering Strategies.</li>
    <li><svg viewBox="0 0 16 16"><circle cx="8" cy="8" r="6.8" fill="none" stroke="#000" stroke-width="1.4"/><path d="M4.5 8.2l2.6 2.6L14 3" fill="none" stroke="#000" stroke-width="1.8"/></svg>We have an average employment retention length of 8 years.</li>
    <li class="narrow"><svg viewBox="0 0 16 16"><circle cx="8" cy="8" r="6.8" fill="none" stroke="#000" stroke-width="1.4"/><path d="M4.5 8.2l2.6 2.6L14 3" fill="none" stroke="#000" stroke-width="1.8"/></svg>We mean business and are dedicated to making your project happen ON TIME, RUN EFFICIENTLY, and we do EXCELLENT WORK.</li>
  </ul>

  <div class="abs divider"></div>

  <h2 class="abs clients-title">Our<br>Clients</h2>
  <ul class="abs client-list clients-a">
    <li>Alder Brothers</li>
    <li>Brightline Precision Group</li>
    <li>North Star Service Corp</li>
    <li>KLR Construction</li>
    <li>Blue Ridge Construction</li>
    <li>Harlow Construction</li>
    <li>Crestfield Heavy<br>Construction</li>
    <li>Fairway Concrete<br>Construction</li>
    <li>Gatepost Interchange<br>Constructors</li>
  </ul>
  <ul class="abs client-list clients-b">
    <li>Greyfield Enterprises</li>
    <li>Keystone Builders</li>
    <li>Dravon • Pelexa</li>
    <li>Max Reiter Brothers</li>
    <li>Maxtell Corporation</li>
    <li>Milford Excavating</li>
    <li>NW Builders</li>
    <li>O’Malley and Sons</li>
    <li>Teller Electric</li>
    <li>Westvale<br>Construction</li>
    <li>Zelson Construction</li>
  </ul>

  <p class="abs safety">EMR<br>Safety<br>rating of<span class="figure">.72</span></p>
  <p class="abs since">SINCE<span class="year">2005</span></p>

  <div class="abs contact">
    <p class="contact-item address">4410 W 62nd Terrace<br>Millbrook, KS 66000
      <svg viewBox="0 0 16 16"><circle cx="8" cy="8" r="8" fill="#c2db2f"/><path d="M4 8.2L8 4.5l4 3.7V12H9.5V9.5h-3V12H4z" fill="#000"/></svg></p>
    <p class="contact-item office office-a">Millbrook Office</p>
    <p class="contact-item phone phone-a">1-555-201-4830
      <svg viewBox="0 0 16 16"><circle cx="8" cy="8" r="8" fill="#c2db2f"/><path d="M5.2 4.2l1.5-.4 1 2.2-1 .8c.5 1.1 1.3 1.9 2.4 2.4l.8-1 2.2 1-.4 1.5c-3.6.2-6.7-2.9-6.5-6.5z" fill="#000"/></svg></p>
    <p class="contact-item office office-b">Riverton Office</p>
    <p class="contact-item phone phone-b">1-555-388-7162
      <svg viewBox="0 0 16 16"><circle cx="8" cy="8" r="8" fill="#c2db2f"/><path d="M5.2 4.2l1.5-.4 1 2.2-1 .8c.5 1.1 1.3 1.9 2.4 2.4l.8-1 2.2 1-.4 1.5c-3.6.2-6.7-2.9-6.5-6.5z" fill="#000"/></svg></p>
    <p class="contact-item web">verdantworksinc.com
      <svg viewBox="0 0 16 16"><circle cx="8" cy="8" r="8" fill="#c2db2f"/><g fill="none" stroke="#000" stroke-width="1"><circle cx="8" cy="8" r="4.5"/><ellipse cx="8" cy="8" rx="2" ry="4.5"/><path d="M3.5 8h9"/></g></svg></p>
  </div>

  <div class="abs brand">
    <p class="brand-name">Verdant Works</p>
    <p class="brand-tag">Landscape and Irrigation</p>
  </div>
</main>
</body>
</html>
```